Geothermal company needs a creative "POW" business card

Manufacturers tend to be boring. We are not! We are a Geothermal Heat Pump company that has over 30 yrs of experience and wants a new look and updated feel. Nothing old (yawn) so get your creative hats on and let's rock!

We want to use the great colors of lime green and navy blue. Our new logo is attached and we're ready to roll. Remember, we're a professional leader in the geothermal industry that needs to make an eye catching and memorable first glance.

```html
<!DOCTYPE html>
<html lang="en">
<head>
<meta charset="utf-8">
<title>Boreal Terra – Business Card</title>
<link rel="stylesheet" href="https://fonts.googleapis.com/css2?family=Open+Sans:wght@400;600;700&family=Archivo+Narrow:wght@500&display=swap">
<style>
  :root {
    --lime: #84fc10;
    --navy: #0f1a6e;
    --ink: #14236b;
    --sky-top: #ffffff;
    --sky-mid: #d8f0fc;
    --sky-bottom: #4dbdf5;
    --globe: #3a7cc4;
    --globe-soft: #9fd2ef;
    --page: #ffffff;
  }
  * { margin: 0; padding: 0; box-sizing: border-box; }
  html, body { width: 1200px; height: 1000px; overflow: hidden; background: var(--page); }
  .canvas { position: relative; width: 1200px; height: 1000px; }

  .card {
    position: absolute;
    width: 1062px;
    height: 620px;
    overflow: hidden;
    background: linear-gradient(180deg, var(--sky-top) 0%, var(--sky-top) 32%, var(--sky-mid) 50%, var(--sky-bottom) 100%);
    box-shadow: 14px 16px 22px rgba(0,0,0,0.45);
  }
  .card--front { left: 70px; top: 58px; }
  .card--back { left: 560px; top: 722px; transform: scale(0.43); transform-origin: 0 0; box-shadow: 20px 24px 30px rgba(0,0,0,0.45); }

  .band-top { position: absolute; left: 0; top: 0; width: 100%; height: 49px; background: var(--lime); }
  .band-bottom { position: absolute; left: 0; bottom: 0; width: 100%; height: 46px; background: var(--navy); }

  .brand-dot { position: absolute; left: 76px; top: 96px; width: 142px; height: 142px; border-radius: 50%; background: var(--globe); }
  .brand-name {
    position: absolute; left: 256px; top: 92px;
    font-family: "Open Sans", sans-serif; font-weight: 700;
    font-size: 80px; line-height: 1; letter-spacing: -2px; color: var(--lime);
    white-space: nowrap;
  }
  .tagline {
    position: absolute; left: 260px; top: 180px;
    font-family: "Archivo Narrow", sans-serif; font-weight: 500;
    font-size: 22px; line-height: 26px; color: var(--ink); white-space: nowrap;
  }
  .reflection {
    position: absolute; left: 256px; top: 210px;
    transform: scaleY(-1); opacity: 0.25;
  }
  .reflection .brand-name, .reflection .tagline { position: static; display: block; }
  .reflection .tagline { padding-left: 4px; color: var(--ink); }
  .corner-mark { position: absolute; right: -70px; top: 340px; width: 220px; height: 220px; border-radius: 50%; background: var(--globe-soft); opacity: 0.85; }

  .contact {
    position: absolute; left: 74px; top: 328px;
    font-family: "Open Sans", sans-serif; font-weight: 400; font-style: normal;
    font-size: 37px; line-height: 46px; letter-spacing: 2.5px; color: var(--ink);
  }
  .contact .dept { font-weight: 600; }

  .label {
    position: absolute;
    font-family: "Open Sans", sans-serif; font-weight: 600;
    font-size: 42px; letter-spacing: 4px; color: var(--navy); white-space: pre;
  }
  .label--front { left: 184px; top: 720px; }
  .label--back { left: 182px; top: 834px; }
</style>
</head>
<body>
<div class="canvas">

  <section class="card card--front">
    <div class="band-top"></div>
    <div class="brand-dot"></div>
    <div class="brand-name">Boreal Terra</div>
    <div class="tagline">Builders of Ground-Source Heat Systems for Cold Climates</div>
    <div class="reflection" aria-hidden="true">
      <div class="tagline">Builders of Ground-Source Heat Systems for Cold Climates</div>
      <div class="brand-name">Boreal Terra</div>
    </div>
    <div class="corner-mark"></div>
    <address class="contact">
      <div class="dept">U.S. Sales</div>
      <div>418 Lakeview Ave.</div>
      <div>Elk Ridge, MN 55999</div>
      <div>ph. 800.555.0147</div>
      <div>info@borealterraheat.com</div>
    </address>
    <div class="band-bottom"></div>
  </section>

  <div class="label label--front">^  Front</div>
  <div class="label label--back">Back&gt;</div>

  <section class="card card--back">
    <div class="band-top"></div>
    <div class="brand-dot"></div>
    <div class="brand-name">Boreal Terra</div>
    <div class="tagline">Builders of Ground-Source Heat Systems for Cold Climates</div>
    <div class="reflection" aria-hidden="true">
      <div class="tagline">Builders of Ground-Source Heat Systems for Cold Climates</div>
      <div class="brand-name">Boreal Terra</div>
    </div>
    <div class="corner-mark"></div>
    <div class="band-bottom"></div>
  </section>

</div>
</body>
</html>
```